Marketing One-Sheet for Security Deposit Claim Notice

I need a one-sheet flyer formatted for email distribution — optimized as a JPEG/PNG that I can insert into Constant Contact or Outlook. I do not want to attach it to an email, but insert it in the email we send out. I would like it to look professional but engaging. Some images would be good, but want to make sure it reads well if images do not load for the recipients. The text is in the attached Word document, but I am open to changes/ideas that may be better for marketing purposes. I included the URLs for some of the links I would like in the one-sheet that is clickable. The logo for the business is being uploaded on the Word document. Proposed text is also uploaded in a Word document. Thank you.

Target Market(s)

Landlords, Real Estate Agents, Property Managers

Industry/Entity Type

Legal

Requirements
Must have
• Professional but appealing design. The One-sheet is going to be placed in the body of emails, not as an attachment.
Nice to have
• Include our logo for the business and the web links please.
Should not have
• Images can be ok, but it needs to look right if images do not download from the email sent out.

```html
<!DOCTYPE html>
<html lang="en">
<head>
<meta charset="utf-8">
<title>Security Deposit Claim Notice</title>
<link href="https://fonts.googleapis.com/css2?family=Prata&family=Oswald:wght@500;600;700&family=Roboto:ital,wght@0,400;0,500;0,700;1,400;1,700&display=swap" rel="stylesheet">
<style>
  :root {
    --red: #b3132b;
    --red-deep: #7a0c1c;
    --red-hero: #c8202f;
    --ink: #111111;
    --text: #2a2a2a;
    --grey-bg: #ededed;
    --grey-line: #d6d6d6;
    --map: #f1f1f1;
    --white: #ffffff;
  }
  * { box-sizing: border-box; margin: 0; padding: 0; }
  html, body { width: 1200px; height: 2192px; overflow: hidden; background: var(--white); }
  body { position: relative; font-family: "Roboto", Arial, sans-serif; color: var(--text); }
  .abs { position: absolute; }

  /* Hero */
  .hero { left: 44px; top: 44px; width: 1112px; height: 744px; overflow: hidden;
    background: linear-gradient(120deg, #d9323c 0%, var(--red-hero) 45%, #a3101f 100%); }
  .hero-photo { left: 0; top: 0; width: 100%; height: 100%;
    background: radial-gradient(ellipse at 80% 55%, rgba(255,255,255,0.28) 0%, rgba(255,255,255,0) 45%),
                radial-gradient(ellipse at 20% 75%, rgba(120,0,10,0.45) 0%, rgba(120,0,10,0) 50%); }
  .hero-kicker { left: 0; top: 108px; width: 100%; text-align: center; color: var(--white);
    font-style: italic; font-size: 38px; }
  .hero-title { left: 0; width: 100%; text-align: center; color: var(--white);
    font-family: "Prata", Georgia, serif; font-size: 138px; line-height: 1; letter-spacing: 1px; white-space: nowrap; }
  .hero-title.first { top: 186px; }
  .hero-title.second { top: 350px; }
  .hero-tag { left: 356px; top: 500px; width: 396px; height: 96px; background: var(--white);
    color: var(--red); font-family: "Oswald", sans-serif; font-weight: 600; font-size: 62px;
    line-height: 96px; text-align: center; }

  /* Middle */
  .state-map { left: 40px; top: 840px; width: 640px; height: 680px;
    background: radial-gradient(ellipse at 45% 45%, var(--map) 0%, rgba(241,241,241,0) 70%); }
  .intro-kicker { left: 84px; top: 900px; font-weight: 700; font-style: italic; font-size: 20px; color: var(--ink); }
  .keep-title { left: 82px; top: 926px; font-family: "Oswald", sans-serif; font-weight: 700;
    font-size: 64px; line-height: 88px; color: var(--ink); text-transform: uppercase; white-space: nowrap; }
  .keep-title .accent { color: var(--red); }
  .uses { left: 96px; top: 1110px; list-style: none; font-size: 23px; line-height: 36px; color: var(--ink); }
  .uses li { display: flex; align-items: center; gap: 18px; }
  .warning { left: 80px; top: 1244px; width: 480px; font-size: 21px; line-height: 32px; color: var(--ink); }

  .risk-card { left: 688px; top: 842px; width: 464px; height: 674px; border: 2px solid var(--grey-line); background: var(--white); }
  .risk-panel { left: 716px; top: 866px; width: 412px; height: 350px;
    background: linear-gradient(135deg, var(--red-deep) 0%, #3d0a10 55%, #1a0507 100%); }
  .risk-item { left: 736px; width: 370px; display: flex; align-items: center; gap: 26px; color: var(--white);
    font-size: 20px; line-height: 26px; }
  .risk-item svg { flex: none; }
  .fee-label { font-family: "Roboto", sans-serif; font-weight: 700; font-size: 28px; line-height: 30px; color: var(--ink); }
  .fee-box { top: 1304px; width: 200px; height: 188px; color: var(--white); text-align: center;
    font-family: "Oswald", sans-serif; font-weight: 700; overflow: hidden; }
  .fee-box.residential { left: 710px; background: var(--red); }
  .fee-box.commercial { left: 926px; background: var(--ink); }
  .fee-box .flat { display: block; margin: 10px auto 0; width: 176px; height: 60px;
    font-size: 42px; line-height: 60px; background: var(--white); color: var(--red); }
  .fee-box.commercial .flat { color: var(--ink); }
  .fee-box .price { display: block; font-size: 84px; line-height: 112px; }

  /* Bottom */
  .cta-band { left: 0; top: 1576px; width: 1200px; height: 544px; background: var(--grey-bg); }
  .cta-wedge { left: 0; top: 1576px; }
  .cta-card { left: 68px; top: 1624px; width: 540px; height: 436px; background: var(--white); text-align: center; }
  .cta-line { position: absolute; left: 0; top: 66px; width: 100%; font-size: 34px; line-height: 40px; font-weight: 500; color: var(--ink); }
  .cta-line .accent { color: var(--red); font-weight: 700; }
  .cta-button { position: absolute; left: 162px; top: 204px; width: 216px; height: 62px; background: var(--red);
    color: var(--white); font-size: 32px; font-weight: 700; line-height: 62px; }
  .cta-contact { position: absolute; left: 0; top: 320px; width: 100%; font-size: 30px; line-height: 36px; color: var(--ink); }

  .brand { left: 700px; top: 1650px; width: 430px; }
  .brand-row { display: flex; align-items: center; gap: 20px; }
  .brand-name { font-family: "Prata", Georgia, serif; font-size: 46px; line-height: 52px; color: var(--red); white-space: nowrap; }
  .brand-square { width: 56px; height: 56px; background: var(--red); flex: none; }
  .brand-sub { font-size: 18px; line-height: 22px; color: var(--red); margin-top: 8px; font-weight: 500; }
  .brand-web { left: 700px; top: 1826px; width: 400px; text-align: center; color: var(--red); font-weight: 700; font-size: 28px; line-height: 36px; }
  .link-btn { top: 1960px; height: 56px; background: var(--red); color: var(--white); font-size: 18px; line-height: 22px;
    text-align: center; display: flex; align-items: center; justify-content: center; }
  .link-btn.info { left: 702px; width: 186px; }
  .link-btn.docs { left: 902px; width: 186px; }

  .footer-bar { left: 0; top: 2140px; width: 1200px; height: 52px; background: var(--red); }
</style>
</head>
<body>

<section class="hero abs">
  <div class="hero-photo abs" role="img" aria-label="Photo of a model house on a table tinted red"></div>
  <p class="hero-kicker abs">We prepare security deposit claim notices</p>
  <h1 class="hero-title first abs">SECURITY</h1>
  <div class="hero-title second abs">DEPOSIT</div>
  <div class="hero-tag abs">CLAIM NOTICE</div>
</section>

<div class="state-map abs" role="img" aria-label="Faint outline map of Florida"></div>
<p class="intro-kicker abs">Follow Florida law to keep the Deposit</p>
<h2 class="keep-title abs"><span class="accent">Keep the</span> Tenant’s<br>Security <span class="accent">Deposit</span></h2>
<ul class="uses abs">
  <li><svg width="22" height="20" viewBox="0 0 22 20"><path d="M2 10l6 6L20 3" fill="none" stroke="#b3132b" stroke-width="4"/></svg>Cover unpaid Rent</li>
  <li><svg width="22" height="20" viewBox="0 0 22 20"><path d="M2 10l6 6L20 3" fill="none" stroke="#b3132b" stroke-width="4"/></svg>Apply to legal fees and costs</li>
  <li><svg width="22" height="20" viewBox="0 0 22 20"><path d="M2 10l6 6L20 3" fill="none" stroke="#b3132b" stroke-width="4"/></svg>Charge against Damages to the Property</li>
</ul>
<p class="warning abs">There are lawyers that specialize in representing tenants and go after landlords that do not make a proper claim against the security deposit. They sue and win their cases and get thousands of dollars in legal fees against Landlords, even if the tenant owes unpaid rent.</p>

<div class="risk-card abs"></div>
<div class="risk-panel abs"></div>
<div class="risk-item abs" style="top:890px">
  <svg width="76" height="76" viewBox="0 0 76 76"><circle cx="38" cy="38" r="34" fill="none" stroke="#fff" stroke-width="4"/><path d="M30 20a20 20 0 1 0 18 0" fill="none" stroke="#fff" stroke-width="3"/><text x="38" y="48" text-anchor="middle" fill="#fff" font-family="Roboto, sans-serif" font-weight="700" font-size="28">$</text></svg>
  <span>Tenant is automatically entitled to their full deposit back</span>
</div>
<div class="risk-item abs" style="top:1002px">
  <svg width="76" height="76" viewBox="0 0 76 76"><circle cx="38" cy="38" r="34" fill="none" stroke="#fff" stroke-width="4"/><text x="38" y="50" text-anchor="middle" fill="#fff" font-family="Roboto, sans-serif" font-weight="700" font-size="34">$</text><line x1="16" y1="16" x2="60" y2="60" stroke="#fff" stroke-width="4"/></svg>
  <span>No claim against the deposit can be made</span>
</div>
<div class="risk-item abs" style="top:1112px">
  <svg width="76" height="76" viewBox="0 0 76 76"><circle cx="38" cy="38" r="34" fill="none" stroke="#fff" stroke-width="4"/><g fill="none" stroke="#fff" stroke-width="3"><line x1="38" y1="20" x2="38" y2="56"/><line x1="22" y1="26" x2="54" y2="26"/><line x1="28" y1="56" x2="48" y2="56"/><path d="M16 42l6-16 6 16z"/><path d="M48 42l6-16 6 16z"/></g></svg>
  <span>Tenant can sue and recover the deposit and thousands in legal fees</span>
</div>
<div class="fee-label abs" style="left:710px;top:1240px">RESIDENTIAL<br>PROPERTIES</div>
<div class="fee-label abs" style="left:926px;top:1240px">COMMERCIAL<br>PROPERTIES</div>
<div class="fee-box residential abs"><span class="flat">FLAT FEE</span><span class="price">$350</span></div>
<div class="fee-box commercial abs"><span class="flat">FLAT FEE</span><span class="price">$450</span></div>

<div class="cta-band abs"></div>
<svg class="cta-wedge abs" width="440" height="544" viewBox="0 0 440 544"><polygon points="0,0 244,0 420,544 0,544" fill="#111111"/></svg>
<div class="cta-card abs">
  <p class="cta-line">Hire us to <span class="accent">prepare and<br>serve to the tenant</span> the<br>security deposit claim!</p>
  <div class="cta-button">Contact Us</div>
  <p class="cta-contact">Tenancy Claim Counsel<br>TenancyClaimCounsel.com</p>
</div>

<div class="brand abs">
  <div class="brand-row"><span class="brand-name">Tenancy Claim<br>Counsel</span><span class="brand-square"></span></div>
  <p class="brand-sub">a Legal Resource for Landlords,<br>Investors &amp; Property Managers</p>
</div>
<p class="brand-web abs">TenancyClaimCounsel.com<br>1(800) 555-0142</p>
<div class="link-btn info abs">More<br>information</div>
<div class="link-btn docs abs">Request our<br>hiring documents</div>

<div class="footer-bar abs"></div>
</body>
</html>
```